Geschäftsunterlagen mit vorhandenem Logo
Zielgruppe
- Immobilienmakler.
- Vermietung und Verkauf von Immobilien
- Eigentümer, Bauträger, Hausverwaltungen, Immobilienentwickler, Wohnungsbaugesellschaften, Käufer und Mieter.
Aufgabenstellung
Wir suchen ein neues Design für unsere Geschäftsunterlagen. Es soll dem Betrachter ein gutes Gefühl vermittelt. Es soll seriös, edel und dynamisch wirken, aber auch vertrauensvoll und kompetent.
Wir suchen neue Designs für folgende Unterlagen, das Logo soll hierbei etwas stärker im Vordergrund stehen :
- Visitenkarten ( Text= Logo, mein Name Jonas Brettler, Handynr. und Webseite )
- Briefpapier ( Text= Logo, Firmenname, Adresse, email, Tel-Nr., event. Bankverbindung ) + Briefumschlag ( Din-Lang ) + email-Vorlage ( Logo + Firmenname, Adresse + Telefon )
- Mappe für Unterlagen ( Din A4 )
- Vermietungsschild und Verkaufsschild fürs Objekt ( 1. H=700mm x B=440mm und 2. H=600 x B 1000mm ) Falls die Schilder zu viel sind, lassen Sie die Entwürfe bitte weg. Priorität haben die anderen Unterlagen.
Logo ist vorhanden, die Schrift kann noch variiert werden.
Falls Sie Fragen haben, schreiben Sie uns bitte an.

```html
<!DOCTYPE html>
<html lang="de">
<head>
<meta charset="utf-8">
<title>Brettler Immobilien – Geschäftsausstattung</title>
<link href="https://fonts.googleapis.com/css2?family=Arimo:wght@400;700&family=Montserrat:wght@500;600;700&display=swap" rel="stylesheet">
<style>
:root{
  --navy:#1e3157;
  --navy-text:#203a6c;
  --sky:#5ab3ea;
  --sky-dark:#3d86c6;
  --paper:#ffffff;
  --ink:#111;
  --frame:#b9c6d8;
}
*{margin:0;padding:0;box-sizing:border-box}
html,body{width:1200px;height:1127px;overflow:hidden;background:#fff}
body{position:relative;font-family:"Arimo",Arial,sans-serif;color:var(--ink)}

.sheet{position:absolute;background:var(--paper);box-shadow:6px 8px 12px rgba(0,0,0,.28);overflow:hidden}

/* brand mark */
.brand{display:flex;align-items:center;font-family:"Montserrat",Arial,sans-serif;font-weight:600;color:var(--navy-text)}
.brand-dot{border-radius:50%;background:currentColor;flex:none}
.brand-name{display:flex;flex-direction:column;line-height:1}
.brand-word{letter-spacing:.5px}
.brand-sub{letter-spacing:1.5px}

/* business card front */
.card-front{left:21px;top:251px;width:343px;height:218px}
.card-front .holder{position:absolute;left:29px;top:12px;font-family:"Montserrat",Arial,sans-serif;font-size:17px;color:var(--navy);letter-spacing:.3px}
.card-front .holder b{font-weight:700}
.card-front .holder span{font-weight:500}
.card-front .brand{position:absolute;left:14px;top:53px}
.card-front .brand-dot{width:36px;height:36px;margin-right:8px}
.card-front .brand-word{font-size:22px}
.card-front .brand-sub{font-size:13px;margin-top:2px}
.card-front svg.bands{position:absolute;left:0;top:0}
.card-contact{position:absolute;display:flex;align-items:center;gap:8px;color:#fff;font-size:6.5px;line-height:1.35}

/* icons */
.ico{width:14px;height:14px;background:#fff;display:flex;align-items:center;justify-content:center;flex:none}
.ico svg{width:10px;height:10px}

/* business card back */
.card-back{left:24px;top:504px;width:341px;height:219px;background:var(--navy)}
.card-back .frame{position:absolute;left:11px;top:11px;right:11px;bottom:11px;border:1.5px solid var(--frame)}
.card-back .brand{position:absolute;left:56px;top:76px;color:#fff}
.card-back .brand-dot{width:60px;height:60px;margin-right:10px}
.card-back .brand-word{font-size:34px}
.card-back .brand-sub{font-size:19px;margin-top:3px}

/* standalone logo */
.logo-standalone{position:absolute;left:78px;top:904px}
.logo-standalone .brand-dot{width:70px;height:70px;margin-right:10px}
.logo-standalone .brand-word{font-size:38px}
.logo-standalone .brand-sub{font-size:21px;margin-top:4px}

/* letterhead */
.letterhead{left:419px;top:107px;width:670px;height:941px}
.letterhead svg.head-band{position:absolute;left:0;top:0}
.letterhead .brand{position:absolute;right:12px;top:3px}
.letterhead .brand-dot{width:30px;height:30px;margin-right:5px}
.letterhead .brand-word{font-size:17px}
.letterhead .brand-sub{font-size:10px;margin-top:1px}
.bank{position:absolute;left:506px;top:116px;font-size:13px;line-height:16px;color:var(--ink)}
.subject{position:absolute;left:80px;top:206px;font-size:12.5px;color:var(--navy-text)}
.letter-body{position:absolute;left:80px;top:250px;width:522px;font-size:11.3px;line-height:20.4px}
.letter-body p{margin-bottom:6px}
.signature{position:absolute;left:80px;top:667px}
.signature-label{position:absolute;left:80px;top:749px;font-size:12.5px;color:var(--navy-text)}
.letterhead svg.foot-band{position:absolute;left:0;bottom:0}
.foot-contacts{position:absolute;left:68px;top:900px;display:flex;gap:20px;color:#fff;font-size:8px;align-items:center}
.foot-contacts .item{display:flex;align-items:center;gap:7px}
</style>
</head>
<body>

<!-- Business card front -->
<section class="sheet card-front">
  <svg class="bands" width="343" height="218" viewBox="0 0 343 218">
    <defs>
      <linearGradient id="skyFront" x1="0" x2="1" y1="0" y2="0">
        <stop offset="0" stop-color="#8fd0f5"/>
        <stop offset="1" stop-color="#3d86c6"/>
      </linearGradient>
    </defs>
    <path d="M0,114 H262 Q276,114 288,121 L343,146 V153 L282,128 Q272,122 262,122 H0Z" fill="url(#skyFront)"/>
    <path d="M0,122 H262 Q272,122 282,128 L343,153 V218 H0Z" fill="#1e3157"/>
  </svg>
  <div class="holder"><b>JONAS</b> <span>BRETTLER</span></div>
  <div class="brand">
    <span class="brand-dot"></span>
    <span class="brand-name"><span class="brand-word">BRETTLER</span><span class="brand-sub">IMMOBILIEN</span></span>
  </div>
  <div class="card-contact" style="left:28px;top:150px">
    <span class="ico"><svg viewBox="0 0 10 10"><path d="M5 0.8a3 3 0 0 1 3 3c0 2.2-3 5.6-3 5.6S2 6 2 3.8a3 3 0 0 1 3-3z" fill="#1e3157"/><circle cx="5" cy="3.8" r="1.1" fill="#fff"/></svg></span>
    <span>2207/45 Linden Street,<br>Hillbrook QLD 4000</span>
  </div>
  <div class="card-contact" style="left:28px;top:181px">
    <span class="ico"><svg viewBox="0 0 10 10"><circle cx="5" cy="5" r="4" fill="none" stroke="#1e3157" stroke-width="1"/><path d="M3.3 3.2l1 -.4.7 1.3-.6.5c.3.7.8 1.2 1.3 1.4l.5-.6 1.3.7-.4 1c-1.9.1-3.9-1.9-3.8-3.9z" fill="#1e3157"/></svg></span>
    <span>0455 81 60927</span>
  </div>
  <div class="card-contact" style="left:148px;top:150px">
    <span class="ico"><svg viewBox="0 0 10 10"><rect x="1" y="2.5" width="8" height="5.5" fill="#1e3157"/><path d="M1 2.5l4 3 4-3" fill="none" stroke="#fff" stroke-width=".8"/></svg></span>
    <span>info@brettler-immo.com.au</span>
  </div>
  <div class="card-contact" style="left:148px;top:181px">
    <span class="ico"><svg viewBox="0 0 10 10"><circle cx="5" cy="5" r="4" fill="#1e3157"/><path d="M1 5h8M5 1c-2 2.5-2 5.5 0 8M5 1c2 2.5 2 5.5 0 8" fill="none" stroke="#fff" stroke-width=".6"/></svg></span>
    <span>www.brettler-immo.com.au</span>
  </div>
</section>

<!-- Business card back -->
<section class="sheet card-back">
  <div class="frame"></div>
  <div class="brand">
    <span class="brand-dot"></span>
    <span class="brand-name"><span class="brand-word">BRETTLER</span><span class="brand-sub">IMMOBILIEN</span></span>
  </div>
</section>

<!-- Standalone logo -->
<div class="brand logo-standalone">
  <span class="brand-dot"></span>
  <span class="brand-name"><span class="brand-word">BRETTLER</span><span class="brand-sub">IMMOBILIEN</span></span>
</div>

<!-- Letterhead -->
<section class="sheet letterhead">
  <svg class="head-band" width="670" height="40" viewBox="0 0 670 40">
    <path d="M0,0 H514 L504,40 H0Z" fill="#1e3157"/>
    <path d="M514,0 H524 L514,40 H504Z" fill="#3d86c6"/>
  </svg>
  <div class="brand">
    <span class="brand-dot"></span>
    <span class="brand-name"><span class="brand-word">BRETTLER</span><span class="brand-sub">IMMOBILIEN</span></span>
  </div>

  <div class="bank">IBAN&nbsp;DE5870312946<br>PIC&nbsp;&nbsp;&nbsp;870312946</div>

  <div class="subject">Subject Line: Loreum ipsum dolor sit amet.</div>

  <div class="letter-body">
    <p>Lorem ipsum dolor sit amet, consectetur adipiscing elit. Maecenas at dapibus diam. Vivamus fringilla nulla lorem, sit amet mollis nisi suscipit in. Donec lacus tortor, finibus eget pharetra vitae, auctor eget augue. Mauris euismod libero ac risus fermentum, sed rhoncus erat consectetur. Phasellus eget hendrerit ligula, id volutpat tellus. Praesent viverra sapien at convallis eleifend. Pellentesque ac ipsum felis. Vestibulum augue massa, blandit eu tellus eu, fringilla volutpat quam.</p>
    <p>Nulla in neque sit amet diam lobortis lacinia. Donec tristique tristique ex in fermentum. Donec tristique erat non turpis sollicitudin, et posuere dui congue. Nulla elementum finibus orci, in varius ligula feugiat ut. Donec viverra hendrerit est, quis pulvinar metus pretium et. Lorem ipsum dolor sit amet, consectetur adipiscing elit. Nulla tempus pretium convallis. Nunc imperdiet tempus sem sit amet rutrum. Morbi tempus in lacus sed sollicitudin. Praesent non sem commodo, faucibus metus id, imperdiet odio. Morbi sodales convallis nulla a rutrum. Class aptent taciti sociosqu ad litora torquent per conubia nostra, per inceptos himenaeos. Nulla condimentum iaculis tellus non scelerisque. Fusce lobortis gravida pretium.</p>
    <p>Cras nec quam mauris. Nulla eu urna eu tortor bibendum eleifend. Nulla imperdiet semper ex, ac iaculis massa consequat eget. Maecenas quis dui varius, tincidunt massa vitae, condimentum lacus. Aliquam in viverra lorem. Integer eros tortor, tristique ac quam in, tempor accumsan lectus. Nulla in neque tellus.</p>
  </div>

  <svg class="signature" width="170" height="72" viewBox="0 0 170 72" role="img" aria-label="Handschriftliche Unterschrift">
    <path d="M18,6 C8,20 4,46 14,52 C22,56 26,30 22,14 C30,30 26,54 32,56 C38,58 36,26 40,22 C42,40 44,56 52,52 C80,42 130,22 166,14" fill="none" stroke="#1e2f7a" stroke-width="1.3"/>
  </svg>
  <div class="signature-label">Signature</div>

  <svg class="foot-band" width="670" height="83" viewBox="0 0 670 83">
    <defs>
      <linearGradient id="skyFoot" x1="0" x2="1" y1="0" y2="0">
        <stop offset="0" stop-color="#8fd0f5"/>
        <stop offset="1" stop-color="#3d86c6"/>
      </linearGradient>
    </defs>
    <path d="M44,9 Q48,0 62,0 H670 V9Z" fill="url(#skyFoot)"/>
    <path d="M0,83 L16,22 Q20,9 38,9 H670 V83Z" fill="#1e3157"/>
  </svg>
  <div class="foot-contacts">
    <span class="item"><span class="ico"><svg viewBox="0 0 10 10"><path d="M5 0.8a3 3 0 0 1 3 3c0 2.2-3 5.6-3 5.6S2 6 2 3.8a3 3 0 0 1 3-3z" fill="#1e3157"/><circle cx="5" cy="3.8" r="1.1" fill="#fff"/></svg></span>2207/45 Linden Street, Hillbrook QLD 4000</span>
    <span class="item"><span class="ico"><svg viewBox="0 0 10 10"><circle cx="5" cy="5" r="4" fill="none" stroke="#1e3157" stroke-width="1"/><path d="M3.3 3.2l1 -.4.7 1.3-.6.5c.3.7.8 1.2 1.3 1.4l.5-.6 1.3.7-.4 1c-1.9.1-3.9-1.9-3.8-3.9z" fill="#1e3157"/></svg></span>0455 81 60927</span>
    <span class="item"><span class="ico"><svg viewBox="0 0 10 10"><rect x="1" y="2.5" width="8" height="5.5" fill="#1e3157"/><path d="M1 2.5l4 3 4-3" fill="none" stroke="#fff" stroke-width=".8"/></svg></span>info@brettler-immo.com.au</span>
    <span class="item"><span class="ico"><svg viewBox="0 0 10 10"><circle cx="5" cy="5" r="4" fill="#1e3157"/><path d="M1 5h8M5 1c-2 2.5-2 5.5 0 8M5 1c2 2.5 2 5.5 0 8" fill="none" stroke="#fff" stroke-width=".6"/></svg></span>www.brettler-immo.com.au</span>
  </div>
</section>

</body>
</html>
```